Brantley Studios photography and video creator

I need a business card for my production company. I shoot photography and videography for real estate, adventure sports and businesses

Contact Information for Business Card

simple not to busy

Colors

Designer to choose colors to be used in the design.

Requirements
Must have
• derek@brantleystudios.ca
• phone -5873304127
• instagram derek_brantley

```html
<!DOCTYPE html>
<html lang="en">
<head>
<meta charset="UTF-8">
<title>Brantley Studios — Business Card</title>
<link href="https://fonts.googleapis.com/css2?family=Montserrat:wght@400;500;600;700;800&display=swap" rel="stylesheet">
<style>
  :root {
    --backdrop: #3a2c28;
    --card-dark: #151515;
    --mountain-light: #e6e6e6;
    --mountain-mid: #8a8a8a;
    --mountain-dark: #2a2a2a;
    --paper: #ffffff;
    --ink: #161616;
    --ink-soft: #6f6f6f;
    --rule: #2a2a2a;
  }
  * { box-sizing: border-box; margin: 0; padding: 0; }
  html, body { width: 1200px; height: 800px; overflow: hidden; }
  body {
    background: var(--backdrop);
    font-family: "Montserrat", sans-serif;
    position: relative;
  }
  .card {
    position: absolute;
    top: 257px;
    width: 500px;
    height: 286px;
    border-radius: 4px;
    overflow: hidden;
    box-shadow: 0 10px 30px rgba(0,0,0,0.35);
  }
  .card--front { left: 70px; background: var(--card-dark); }
  .card--back { left: 630px; background: var(--paper); }

  .front-scene {
    position: absolute;
    inset: 0;
    background: linear-gradient(210deg, var(--mountain-light) 0%, var(--mountain-mid) 30%, var(--mountain-dark) 58%, var(--card-dark) 80%);
  }
  .front-wordmark {
    position: absolute;
    left: 34px;
    bottom: 62px;
    color: var(--paper);
    font-weight: 700;
    font-size: 40px;
    letter-spacing: 1px;
    text-transform: uppercase;
    line-height: 1;
  }

  .back-badge {
    position: absolute;
    left: 40px;
    top: 78px;
    width: 130px;
    height: 130px;
    border-radius: 50%;
    background: var(--card-dark);
    display: flex;
    align-items: center;
    justify-content: center;
    text-align: center;
  }
  .back-badge__name {
    color: var(--paper);
    font-weight: 700;
    font-size: 15px;
    line-height: 1.2;
    text-transform: uppercase;
    letter-spacing: 0.5px;
  }
  .back-divider {
    position: absolute;
    left: 212px;
    top: 82px;
    width: 1.5px;
    height: 120px;
    background: var(--rule);
  }
  .contact {
    position: absolute;
    left: 232px;
    top: 84px;
    color: var(--ink);
  }
  .contact__name {
    font-size: 20px;
    font-weight: 700;
    line-height: 1.1;
  }
  .contact__first { color: var(--ink-soft); }
  .contact__role {
    font-size: 12px;
    font-weight: 500;
    margin-bottom: 12px;
  }
  .contact__list { list-style: none; }
  .contact__item {
    display: flex;
    align-items: center;
    gap: 7px;
    font-size: 14px;
    font-weight: 500;
    line-height: 1.35;
  }
  .contact__icon { width: 12px; height: 12px; flex: none; }
</style>
</head>
<body>
  <section class="card card--front" aria-label="Business card front">
    <div class="front-scene" role="img" aria-label="Greyscale mountain range illustration with evergreen trees"></div>
    <div class="front-wordmark">Brantley Studios</div>
  </section>

  <section class="card card--back" aria-label="Business card back">
    <div class="back-badge">
      <span class="back-badge__name">Brantley<br>Studios</span>
    </div>
    <div class="back-divider"></div>
    <div class="contact">
      <p class="contact__name"><span class="contact__first">Derek</span> Brantley</p>
      <p class="contact__role">Manager</p>
      <ul class="contact__list">
        <li class="contact__item">
          <svg class="contact__icon" viewBox="0 0 24 24" aria-hidden="true"><path fill="#161616" d="M6.6 10.8c1.4 2.8 3.8 5.1 6.6 6.6l2.2-2.2c.3-.3.7-.4 1-.2 1.1.4 2.3.6 3.6.6.6 0 1 .4 1 1V20c0 .6-.4 1-1 1C10.6 21 3 13.4 3 4c0-.6.4-1 1-1h3.5c.6 0 1 .4 1 1 0 1.3.2 2.5.6 3.6.1.3 0 .7-.2 1z"/></svg>
          5873304127
        </li>
        <li class="contact__item">
          <svg class="contact__icon" viewBox="0 0 24 24" aria-hidden="true"><rect x="3" y="3" width="18" height="18" rx="4" fill="none" stroke="#161616" stroke-width="2.2"/></svg>
          derek_brantley
        </li>
        <li class="contact__item">
          <svg class="contact__icon" viewBox="0 0 24 24" aria-hidden="true"><rect x="2" y="5" width="20" height="14" fill="#161616"/><path d="M2 5l10 8 10-8" fill="none" stroke="#fff" stroke-width="1.6"/></svg>
          derek@brantleystudios.ca
        </li>
      </ul>
    </div>
  </section>
</body>
</html>
```